TOPページのイメージを作成していただきたいです。
女性が入りやすく、親しみやすい色使いとフォントで、
カテゴリのボタンはアイコン等を使い、やわらかい印象を与えたい
※アイコンを指定しているわけではありません。

商品にカラフルなものが多くなりやすいので、全体的な色バランスはシンプルなカラーでお願いします。
サイドバナーとメインに上記スクールをターゲットとしたカテゴリに飛ぶためのバナー用意してほしいです。
近いサイトイメージは合わせて送らせていただきます。
スマートフォンでも表示させやすいレイアウトを希望します。
Quelvoのショッピングに関しては、Quelvoプリズマを契約予定です。
また、今回はトップページだけですが、契約させて頂いた方には商品ページなどサブページも依頼する可能性が高いです

-------------------
項目について
-------------------
※スプレッドシート参照
https://sheets.tavrolink.com/spreadsheets/d/7pxQwLzNc4bTr2VhYk9MeJsA8uDfGiHo3nKyRtE5WqPl/edit?usp=sharing
■ヘッダー
検索窓、お支払いについて、送料、お届けについて、返品、交換、保証について、会社概要、プライバシーポリシー、お問い合わせ、よくある質問
■フッター
店舗内簡易情報として、イメージ画像のような下記の内容を用意する予定で、記述箇所のデザインを用意してください
送料について、支払い方法について、手数料、納期、キャンセルについて、商品の在庫について
■カテゴリ
カテゴリは、別紙の資料の通りです。
大カテゴリがメイン、中に小カテゴリがあります。

■写真資料
https://files.tavrolink.com/file/d/9kd3RwQ7mZ2xVbN8pLcT4yHsJfGeAu6Wn/view?usp=sharing

■サイト見本イメージ
https://store.mirubeta.jp/pastelnook/
https://yarn-lumio.com/
https://ec.stitchvale.jp/
https://www.tomiseki.co.jp/shop/c/c10/
https://www.webshop.mirel-kasano.com/
https://works.brevok.net/
サイトの色合いや雰囲気に近いサイトになります。
1ページ
赤系、黄・オレンジ系、茶系
• イラストレーター形式 (.ai)
幅1250px程度
※Quelvoショップのバナーサイズを考慮しています。
場合によってはその他のページもお願いする可能性があります。
もう少し提案数を頂きたいため、5月13日(金)までコンペの延長をいたします。

今回選ばせていただきました理由は
・商品を邪魔しないシンプルさ
・Quelvoショップに落とし込んだ時に差異が生まれにくい点
・全体的な色使い
を中心に選ばせていただきました。
非常にあたたかく、親しみやすいデザインで作成いただきましたので、こちらに決定させていただきました。

今回いただきました提案はどれも素晴らしく、選考は非常に悩みました。
冒険するか、無難なデザインにするか、また、その中でもどれがいいか、かなり悩みまして、選ばれなかったデザインも、最後までの残ったデザインがいくつかございました。
本当に皆様ご提案ありがとうございました。
また次の機会がございましたら、是非よろしくお願いします。

```html
<!DOCTYPE html>
<html lang="ja">
<head>
<meta charset="utf-8">
<title>ぬいとこ | ハンドメイドショップ</title>
<link href="https://fonts.googleapis.com/css2?family=M+PLUS+Rounded+1c:wght@400;500;700&family=Cormorant+Garamond:ital,wght@0,500;1,500&display=swap" rel="stylesheet">
<style>
:root{
  --ink:#4a403a;
  --ink-soft:#7a6e66;
  --taupe:#8c7d73;
  --taupe-dark:#6f6158;
  --beige:#ece5dc;
  --beige-soft:#f5f1ec;
  --line:#d9d1c8;
  --price:#c2443a;
  --footer:#e7e3de;
  --white:#ffffff;
}
*{box-sizing:border-box;margin:0;padding:0}
html,body{width:1200px;height:2884px;overflow:hidden}
body{position:relative;background:var(--white);color:var(--ink);font-family:"M PLUS Rounded 1c",sans-serif;font-size:13px}
a{color:inherit;text-decoration:none}
.serif{font-family:"Cormorant Garamond",serif}
.photo{display:block;background:linear-gradient(135deg,#d8cfc4,#b9aca0)}

/* header */
.site-header{position:absolute;left:0;top:0;width:1200px;height:110px}
.brand{position:absolute;left:36px;top:22px}
.brand-tag{font-size:12px;color:var(--ink-soft);letter-spacing:.1em}
.brand-name{font-size:38px;font-weight:500;letter-spacing:.08em;line-height:1.2}
.global-nav{position:absolute;right:32px;top:26px;display:flex}
.global-nav a{font-size:12px;padding:4px 12px;border-left:1px solid var(--line)}
.global-nav a:last-child{border-right:1px solid var(--line)}

/* hero */
.hero{position:absolute;left:0;top:160px;width:1200px;height:320px;background:var(--beige);overflow:hidden}
.hero-left{position:absolute;left:0;top:0;width:390px;height:320px;background:linear-gradient(160deg,#f1ece5 0%,#cfc3b6 55%,#8a7466 100%)}
.hero-right{position:absolute;right:0;top:0;width:400px;height:320px;background:linear-gradient(200deg,#e9e2d8 0%,#9b8d84 55%,#5d5450 100%)}
.hero-copy{position:absolute;left:390px;width:410px;top:0;height:320px;text-align:center;padding-top:70px}
.hero-en{font-size:22px;letter-spacing:.2em;color:var(--ink-soft)}
.hero-title{font-size:38px;font-weight:500;letter-spacing:.08em;margin:14px 0 18px;padding-bottom:16px;border-bottom:1px solid var(--taupe)}
.hero-lead{font-size:13px;line-height:1.8;color:var(--ink-soft)}
.hero-dots{position:absolute;left:0;top:506px;width:1200px;display:flex;justify-content:center;gap:10px}
.hero-dots span{width:9px;height:9px;border-radius:50%;background:var(--line)}
.hero-dots span:first-child{background:var(--taupe)}

/* sidebar */
.sidebar{position:absolute;left:32px;top:580px;width:216px}
.side-banner{display:block;border:1px solid var(--line);background:var(--beige-soft)}
.side-banner .photo{height:110px;background:linear-gradient(150deg,#efe9e1,#b5a598 60%,#6e6259)}
.side-banner-body{text-align:center;padding:12px 10px 16px}
.side-banner-title{font-size:22px;line-height:1.35;font-weight:500}
.side-banner-text{font-size:11px;color:var(--ink-soft);margin-top:8px;line-height:1.6}
.side-search{display:flex;margin-top:40px;height:30px}
.side-search input{flex:1;border:1px solid var(--line);font-family:inherit;padding:0 8px}
.side-search button{width:48px;border:none;background:var(--taupe);color:var(--white);font-family:inherit;font-size:12px}
.cat-nav{margin-top:22px}
.cat-group{margin-bottom:6px}
.cat-head{display:flex;align-items:center;gap:8px;height:28px;padding:0 10px;background:var(--taupe);color:var(--white);font-size:13px;border-radius:3px}
.cat-head svg{width:14px;height:14px;flex:none}
.cat-list{list-style:none;padding:2px 0 0 18px}
.cat-list li{font-size:12px;line-height:18px;color:var(--ink-soft)}
.cat-list li::before{content:"›";margin-right:6px;color:var(--taupe)}

/* main */
.main{position:absolute;left:300px;top:580px;width:868px}
.sec-title{text-align:center}
.sec-title .en{display:flex;align-items:center;justify-content:center;gap:18px;font-size:32px;line-height:1}
.sec-title .en::before,.sec-title .en::after{content:"";width:240px;height:1px;background:var(--line)}
.sec-title .ja{display:block;font-size:11px;color:var(--ink-soft);margin-top:6px}
.grid3{position:absolute;left:20px;width:848px;display:flex;gap:36px}
.grid3 .item{width:256px}
.grid3 .photo{height:240px}
.item-name{text-align:center;font-size:12px;margin-top:16px}
.item-price{text-align:center;font-size:15px;color:var(--price);margin-top:4px}
.item-price small{font-size:10px;color:var(--ink-soft)}
.grid5{position:absolute;left:20px;width:848px;display:flex;gap:24px}
.grid5 .item{width:150px;position:relative}
.grid5 .photo{height:150px;margin-top:34px}
.rank{position:absolute;top:0;left:0;width:150px;display:flex;justify-content:center;align-items:flex-end;gap:4px;font-size:16px;color:var(--taupe-dark)}
.rank svg{width:26px;height:22px}

.banners{position:absolute;left:20px;top:1360px;width:848px;display:flex;gap:20px}
.banner{position:relative;height:220px;flex:1;overflow:hidden}
.banner-event{background:linear-gradient(120deg,#5a524d,#a99e95 60%,#d9d0c6)}
.banner-kit{background:linear-gradient(120deg,#f1ede8,#c8c0b8 55%,#5f6e8a)}
.banner-label{position:absolute;font-size:40px;font-style:italic;line-height:1}
.banner-label small{display:block;font-family:"M PLUS Rounded 1c",sans-serif;font-style:normal;font-size:12px;margin-top:6px}
.banner-event .banner-label{right:40px;top:70px;color:var(--white)}
.banner-kit .banner-label{left:40px;top:120px;color:var(--ink)}

.guide-title{position:absolute;left:0;top:1612px;width:868px}
.guide-title .en{font-family:"M PLUS Rounded 1c",sans-serif;font-size:20px;font-weight:500}
.guide{position:absolute;left:20px;top:1670px;width:848px;display:flex;gap:16px}
.guide a{flex:1;display:flex;align-items:center;gap:12px;height:70px;padding:0 12px;border:1px solid var(--line)}
.guide .ico{width:46px;height:46px;border-radius:50%;background:var(--beige);display:flex;align-items:center;justify-content:center;flex:none}
.guide .ico svg{width:24px;height:24px}
.guide span{font-size:12px;line-height:1.5}

/* footer */
.site-footer{position:absolute;left:0;top:2420px;width:1200px;height:420px;background:var(--footer)}
.foot-cols{display:flex;gap:40px;padding:44px 40px 0}
.foot-col{flex:1}
.foot-col h3{font-size:13px;font-weight:500;padding-bottom:8px;margin-bottom:10px;border-bottom:1px solid var(--taupe)}
.foot-col p{font-size:11px;line-height:1.9;color:var(--ink-soft);margin-bottom:20px}
.copyright{position:absolute;left:0;top:2840px;width:1200px;height:44px;background:var(--taupe);color:var(--white);font-size:11px;text-align:center;line-height:44px}
</style>
</head>
<body>

<header class="site-header">
  <a class="brand" href="#">
    <p class="brand-tag">ハンドメイドショップ</p>
    <p class="brand-name">ぬいとこ</p>
  </a>
  <nav class="global-nav">
    <a href="#">お支払いについて</a>
    <a href="#">送料、お届けについて</a>
    <a href="#">返品、交換、保証について</a>
    <a href="#">会社概要</a>
    <a href="#">プライバシーポリシー</a>
    <a href="#">お問い合わせ</a>
    <a href="#">よくある質問</a>
  </nav>
</header>

<section class="hero">
  <div class="hero-left" role="img" aria-label="花柄を刺繍したトートバッグと手芸道具の写真"></div>
  <div class="hero-copy">
    <p class="hero-en serif">HANDMADE SCHOOL</p>
    <h1 class="hero-title">ハンドメイド作家になる</h1>
    <p class="hero-lead">好きな時間を上手に使うハンドメイド作家への第一歩。<br>スクール開講しております。</p>
  </div>
  <div class="hero-right" role="img" aria-label="刺繍入りのバッグと布小物を並べた写真"></div>
</section>
<div class="hero-dots"><span></span><span></span><span></span><span></span><span></span></div>

<aside class="sidebar">
  <a class="side-banner" href="#">
    <div class="photo" role="img" aria-label="刺繍のトートバッグの写真"></div>
    <div class="side-banner-body">
      <p class="side-banner-title">ハンドメイド<br>作家になる</p>
      <p class="side-banner-text">好きな時間を上手に使う<br>作家への第一歩を応援します。</p>
    </div>
  </a>
  <form class="side-search"><input type="text" aria-label="検索"><button type="button">検索</button></form>

  <nav class="cat-nav">
    <div class="cat-group"><p class="cat-head"><svg viewBox="0 0 14 14"><circle cx="7" cy="7" r="5" fill="none" stroke="#fff" stroke-width="1.5"/></svg>裁縫用品</p>
      <ul class="cat-list"><li>アイロン用品</li><li>お裁縫道具セット</li><li>ミシン糸・手縫い糸</li></ul></div>
    <div class="cat-group"><p class="cat-head"><svg viewBox="0 0 14 14"><rect x="2" y="2" width="10" height="10" rx="2" fill="none" stroke="#fff" stroke-width="1.5"/></svg>生地・テープ・リボン</p>
      <ul class="cat-list"><li>プリント生地</li><li>無地生地</li><li>ワッペン</li><li>テープ・リボン</li><li>フェルト</li></ul></div>
    <div class="cat-group"><p class="cat-head"><svg viewBox="0 0 14 14"><circle cx="7" cy="7" r="5" fill="none" stroke="#fff" stroke-width="1.5"/><circle cx="7" cy="7" r="1.5" fill="#fff"/></svg>刺繍用品</p>
      <ul class="cat-list"><li>刺繍糸</li><li>刺繍枠</li><li>図案シート</li></ul></div>
    <div class="cat-group"><p class="cat-head"><svg viewBox="0 0 14 14"><circle cx="7" cy="7" r="5" fill="none" stroke="#fff" stroke-width="1.5"/><circle cx="5.5" cy="5.5" r="1" fill="#fff"/><circle cx="8.5" cy="8.5" r="1" fill="#fff"/></svg>手芸パーツ</p>
      <ul class="cat-list"><li>ボタン</li><li>ファスナー</li><li>ゴム・ひも</li><li>スナップ</li><li>ハトメ</li><li>持ち手</li></ul></div>
    <div class="cat-group"><p class="cat-head"><svg viewBox="0 0 14 14"><path d="M3 5h8l-1 7H4z" fill="none" stroke="#fff" stroke-width="1.5"/></svg>布小物</p>
      <ul class="cat-list"><li>ポーチ</li><li>エコバッグ</li><li>コースター</li><li>ハンカチ</li><li>巾着</li></ul></div>
    <div class="cat-group"><p class="cat-head"><svg viewBox="0 0 14 14"><circle cx="4" cy="7" r="2" fill="#fff"/><circle cx="10" cy="7" r="2" fill="#fff"/></svg>ビーズ</p>
      <ul class="cat-list"><li>ガラスビーズ</li><li>ウッドビーズ</li></ul></div>
    <div class="cat-group"><p class="cat-head"><svg viewBox="0 0 14 14"><path d="M7 2l4 5-4 5-4-5z" fill="none" stroke="#fff" stroke-width="1.5"/></svg>アクセサリー</p>
      <ul class="cat-list"><li>金具パーツ</li><li>チェーン</li><li>ピアス・イヤリング</li></ul></div>
    <div class="cat-group"><p class="cat-head"><svg viewBox="0 0 14 14"><path d="M7 2c3 4 4 6 4 7.5a4 4 0 0 1-8 0C3 8 4 6 7 2z" fill="none" stroke="#fff" stroke-width="1.5"/></svg>レジン</p>
      <ul class="cat-list"><li>UVレジン液</li><li>シリコンモールド</li><li>封入パーツ</li><li>着色料</li></ul></div>
    <div class="cat-group"><p class="cat-head"><svg viewBox="0 0 14 14"><rect x="3" y="7" width="8" height="5" fill="none" stroke="#fff" stroke-width="1.5"/><rect x="5.5" y="2" width="3" height="5" fill="#fff"/></svg>スタンプ作成</p>
      <ul class="cat-list"><li>消しゴムはんこ</li><li>インク</li></ul></div>
    <div class="cat-group"><p class="cat-head"><svg viewBox="0 0 14 14"><rect x="2" y="4" width="10" height="7" rx="1" fill="none" stroke="#fff" stroke-width="1.5"/></svg>レザー作成</p>
      <ul class="cat-list"><li>革はぎれ</li><li>レザー工具</li></ul></div>
    <div class="cat-group"><p class="cat-head"><svg viewBox="0 0 14 14"><path d="M3 2h6l2 2v8H3z" fill="none" stroke="#fff" stroke-width="1.5"/></svg>ペーパークラフト</p>
      <ul class="cat-list"><li>和紙</li><li>包装紙</li><li>マスキングテープ</li></ul></div>
    <div class="cat-group"><p class="cat-head"><svg viewBox="0 0 14 14"><path d="M4 2h6v4a3 3 0 0 1-6 0z M7 9v3" fill="none" stroke="#fff" stroke-width="1.5"/></svg>ガラス細工</p>
      <ul class="cat-list"><li>ガラス絵具</li><li>ステンドパーツ</li></ul></div>
    <div class="cat-group"><p class="cat-head"><svg viewBox="0 0 14 14"><path d="M7 1.5l1.6 3.4 3.7.4-2.8 2.5.8 3.7L7 9.6 3.7 11.5l.8-3.7L1.7 5.3l3.7-.4z" fill="#fff"/></svg>イベントキット</p>
      <ul class="cat-list"><li>クリスマス</li><li>ハロウィン</li><li>夏休み工作</li></ul></div>
    <div class="cat-group"><p class="cat-head"><svg viewBox="0 0 14 14"><rect x="2" y="5" width="10" height="7" fill="none" stroke="#fff" stroke-width="1.5"/><path d="M2 5h10M7 5v7" stroke="#fff" stroke-width="1.5"/></svg>スタートキット</p>
      <ul class="cat-list"><li>ソーイング</li><li>刺繍</li><li>レジン</li><li>編み物</li></ul></div>
  </nav>
</aside>

<main class="main">
  <section>
    <div class="sec-title" style="position:absolute;left:0;top:12px;width:868px"><p class="en serif">Pick Up Item</p><span class="ja">おすすめアイテム</span></div>
    <div class="grid3" style="top:80px">
      <a class="item" href="#"><span class="photo" role="img" aria-label="刺繍入りの白いバッグの写真" style="background:linear-gradient(135deg,#7a6e66,#d8d2ca 55%,#f2eeea)"></span><p class="item-name">商品名が入ります。</p><p class="item-price">1000円<small>(税込)</small></p></a>
      <a class="item" href="#"><span class="photo" role="img" aria-label="ステッチ入りの布巾を並べた写真" style="background:linear-gradient(135deg,#a89583,#ece6de 55%,#c9bcb0)"></span><p class="item-name">商品名が入ります。</p><p class="item-price">1000円<small>(税込)</small></p></a>
      <a class="item" href="#"><span class="photo" role="img" aria-label="緑のミトンの写真" style="background:linear-gradient(135deg,#3f4b3c,#6f9a52 55%,#a7c277)"></span><p class="item-name">商品名が入ります。</p><p class="item-price">1000円<small>(税込)</small></p></a>
    </div>
  </section>

  <section>
    <div class="sec-title" style="position:absolute;left:0;top:472px;width:868px"><p class="en serif">Ranking</p><span class="ja">人気ランキング</span></div>
    <div class="grid5" style="top:526px">
      <a class="item" href="#"><p class="rank"><svg viewBox="0 0 26 22"><path d="M2 18L4 6l5 5 4-8 4 8 5-5 2 12z" fill="#c9a24b"/></svg>1</p><span class="photo" role="img" aria-label="刺繍入りの布小物の写真" style="background:linear-gradient(135deg,#e9e4dd,#9aa3a6)"></span><p class="item-name">商品名が入ります。</p><p class="item-price">1000円<small>(税込)</small></p></a>
      <a class="item" href="#"><p class="rank"><svg viewBox="0 0 26 22"><path d="M2 18L4 6l5 5 4-8 4 8 5-5 2 12z" fill="#a8a8ad"/></svg>2</p><span class="photo" role="img" aria-label="デニムのジャケットの写真" style="background:linear-gradient(135deg,#3f5472,#8ea0b8)"></span><p class="item-name">商品名が入ります。</p><p class="item-price">1000円<small>(税込)</small></p></a>
      <a class="item" href="#"><p class="rank"><svg viewBox="0 0 26 22"><path d="M2 18L4 6l5 5 4-8 4 8 5-5 2 12z" fill="#b98559"/></svg>3</p><span class="photo" role="img" aria-label="刺繍パーツを並べた写真" style="background:linear-gradient(135deg,#ece7e0,#c95c4c 60%,#6e4b3d)"></span><p class="item-name">商品名が入ります。</p><p class="item-price">1000円<small>(税込)</small></p></a>
      <a class="item" href="#"><p class="rank">4</p><span class="photo" role="img" aria-label="刺繍入りのトップスの写真" style="background:linear-gradient(135deg,#2f3a4d,#6d7b93)"></span><p class="item-name">商品名が入ります。</p><p class="item-price">1000円<small>(税込)</small></p></a>
      <a class="item" href="#"><p class="rank">5</p><span class="photo" role="img" aria-label="刺繍を施したバッグの写真" style="background:linear-gradient(135deg,#f0ece6,#b7c6d6)"></span><p class="item-name">商品名が入ります。</p><p class="item-price">1000円<small>(税込)</small></p></a>
    </div>
  </section>

  <section>
    <div class="sec-title" style="position:absolute;left:0;top:832px;width:868px"><p class="en serif">New Item</p><span class="ja">新着アイテム</span></div>
    <div class="grid3" style="top:920px">
      <a class="item" href="#"><span class="photo" role="img" aria-label="文字刺繍の白いTシャツの写真" style="background:linear-gradient(135deg,#f3f1ee,#d6d0c9)"></span><p class="item-name">商品名が入ります。</p><p class="item-price">1000円<small>(税込)</small></p></a>
      <a class="item" href="#"><span class="photo" role="img" aria-label="茶色の革のショルダーバッグの写真" style="background:linear-gradient(135deg,#efe9e2,#b06a3b 55%,#6d3f22)"></span><p class="item-name">商品名が入ります。</p><p class="item-price">1000円<small>(税込)</small></p></a>
      <a class="item" href="#"><span class="photo" role="img" aria-label="文字入りの白いエプロンの写真" style="background:linear-gradient(135deg,#e7e3de,#f8f7f5 50%,#cfc9c2)"></span><p class="item-name">商品名が入ります。</p><p class="item-price">1000円<small>(税込)</small></p></a>
    </div>
  </section>

  <div class="banners">
    <a class="banner banner-event" href="#" role="img" aria-label="工作をする子どもの手元の写真"><p class="banner-label serif">Event<small>イベントキット</small></p></a>
    <a class="banner banner-kit" href="#" role="img" aria-label="花の刺繍とはじめてキットの写真"><p class="banner-label serif">Start kit<small>スタートキット</small></p></a>
  </div>

  <div class="sec-title guide-title"><p class="en">初めてのかたへ</p></div>
  <div class="guide">
    <a href="#"><span class="ico"><svg viewBox="0 0 24 24"><path d="M3 5h3l2 10h10l2-7H7" fill="none" stroke="#8c7d73" stroke-width="1.8"/><circle cx="9" cy="19" r="1.5" fill="#8c7d73"/><circle cx="17" cy="19" r="1.5" fill="#8c7d73"/></svg></span><span>ご注文の流れに<br>ついて</span></a>
    <a href="#"><span class="ico"><svg viewBox="0 0 24 24"><rect x="3" y="6" width="18" height="12" rx="2" fill="none" stroke="#8c7d73" stroke-width="1.8"/><path d="M3 10h18" stroke="#8c7d73" stroke-width="1.8"/></svg></span><span>お支払い方法に<br>ついて</span></a>
    <a href="#"><span class="ico"><svg viewBox="0 0 24 24"><path d="M4 8l8-4 8 4v9l-8 4-8-4z M4 8l8 4 8-4 M12 12v9" fill="none" stroke="#8c7d73" stroke-width="1.8"/></svg></span><span>商品のお届けに<br>ついて</span></a>
    <a href="#"><span class="ico"><svg viewBox="0 0 24 24"><circle cx="12" cy="8" r="4" fill="none" stroke="#8c7d73" stroke-width="1.8"/><path d="M4 21c1-5 15-5 16 0" fill="none" stroke="#8c7d73" stroke-width="1.8"/></svg></span><span>会員登録の<br>ご案内</span></a>
  </div>
</main>

<footer class="site-footer">
  <div class="foot-cols">
    <div class="foot-col"><h3>送料について</h3><p>テキストが入ります。テキストが入ります。テキストが入ります。テキストが入ります。テキストが入ります。テキストが入ります。</p></div>
    <div class="foot-col"><h3>支払い方法について</h3><p>テキストが入ります。テキストが入ります。テキストが入ります。テキストが入ります。テキストが入ります。テキストが入ります。</p></div>
    <div class="foot-col"><h3>手数料</h3><p>テキストが入ります。テキストが入ります。テキストが入ります。</p><h3>納期</h3><p>テキストが入ります。テキストが入ります。テキストが入ります。</p></div>
    <div class="foot-col"><h3>キャンセルについて</h3><p>テキストが入ります。テキストが入ります。テキストが入ります。</p><h3>商品の在庫について</h3><p>テキストが入ります。テキストが入ります。テキストが入ります。</p></div>
  </div>
</footer>
<p class="copyright">Copyright (c) ぬいとこ All Rights Reserved.</p>

</body>
</html>
```